Business Management Fortress

Assist with enhancing a powerpoint slide by providing a few design options for consideration. I have a template but open to any creative ideas.

Target Market(s)

Internal employees and stakeholders

Industry/Entity Type

Business Management, Finance, Accounting

Requirements
Must have
• Maintain a fortress, temple, or pyramid schema
Nice to have
• Scenic Background

```html
<!DOCTYPE html>
<html lang="en">
<head>
<meta charset="utf-8">
<title>Fiduciary Responsibilities</title>
<link href="https://fonts.googleapis.com/css2?family=Raleway:wght@400;500;700;800&display=swap" rel="stylesheet">
<style>
  :root {
    --page-bg: #b4c6dc;
    --slide-dark: #262626;
    --panel-blue: #3d7aa8;
    --gold: #f4b400;
    --white: #ffffff;
    --icon-ink: #262626;
  }
  html, body {
    margin: 0;
    padding: 0;
    width: 1200px;
    height: 1200px;
    overflow: hidden;
    background: var(--page-bg);
    font-family: "Raleway", sans-serif;
  }
  .slide {
    position: absolute;
    left: 0;
    top: 263px;
    width: 1200px;
    height: 674px;
    display: block;
  }
  .label { font-family: "Raleway", sans-serif; font-weight: 700; fill: var(--white); text-anchor: middle; }
  .label-caps { font-size: 21px; }
  .label-tile { font-size: 20px; }
  .title { font-family: "Raleway", sans-serif; font-weight: 800; font-size: 38px; fill: var(--white); }
  .duty { font-family: "Raleway", sans-serif; font-weight: 500; font-size: 25px; fill: var(--white); }
  .tick { fill: none; stroke: var(--white); stroke-width: 2.6; stroke-linecap: round; stroke-linejoin: round; }
  .icon-light { fill: #fff4e6; }
  .icon-line { fill: none; stroke: #fff4e6; stroke-width: 2.4; stroke-linecap: round; stroke-linejoin: round; }
</style>
</head>
<body>
<svg class="slide" viewBox="0 0 1232 692" xmlns="http://www.w3.org/2000/svg" role="group" aria-label="Fiduciary responsibilities slide">
  <defs>
    <linearGradient id="leader-grad" x1="0" y1="0" x2="1" y2="1">
      <stop offset="0" stop-color="#9fd0f2"/>
      <stop offset="0.5" stop-color="#5aaee0"/>
      <stop offset="1" stop-color="#3a78b4"/>
    </linearGradient>
    <linearGradient id="leader-band" x1="0" y1="0" x2="1" y2="0">
      <stop offset="0" stop-color="#8cc3ea"/>
      <stop offset="1" stop-color="#3a74ae"/>
    </linearGradient>
    <linearGradient id="partner-grad" x1="0" y1="0" x2="1" y2="1">
      <stop offset="0" stop-color="#c8174c"/>
      <stop offset="1" stop-color="#ee4c7c"/>
    </linearGradient>
    <linearGradient id="partner-band" x1="0" y1="0" x2="1" y2="0">
      <stop offset="0" stop-color="#d21c50"/>
      <stop offset="1" stop-color="#f04d7f"/>
    </linearGradient>
    <linearGradient id="profit-grad" x1="0" y1="0" x2="1" y2="1">
      <stop offset="0" stop-color="#8ee896"/>
      <stop offset="0.5" stop-color="#4fd078"/>
      <stop offset="1" stop-color="#2e9a46"/>
    </linearGradient>
    <linearGradient id="profit-band" x1="0" y1="0" x2="1" y2="0">
      <stop offset="0" stop-color="#8ee38a"/>
      <stop offset="1" stop-color="#2f9e48"/>
    </linearGradient>
  </defs>

  <!-- backgrounds -->
  <rect class="slide-left" x="0" y="0" width="741" height="692" fill="var(--slide-dark)"/>
  <rect class="slide-panel" x="741" y="0" width="491" height="692" fill="var(--panel-blue)"/>

  <!-- pillar: leader -->
  <g class="pillar pillar-leader">
    <path d="M198 112 L351 348 L41 348 Z M198 202 L133 303 L262 303 Z" fill="url(#leader-grad)" fill-rule="evenodd"/>
    <path d="M70 303 L322 303 L351 348 L41 348 Z" fill="url(#leader-band)"/>
    <text class="label label-caps" x="198" y="334">LEADER</text>
    <g class="icon" transform="translate(198 262)">
      <circle class="icon-light" cx="-6" cy="-16" r="4"/>
      <path class="icon-line" d="M-6 -10 V6 M-11 -6 H-1 M-9 6 V18 M-3 6 V18"/>
      <path class="icon-line" d="M7 -22 V18"/>
      <path class="icon-light" d="M7 -22 H18 L15 -18 L18 -14 H7 Z"/>
    </g>
  </g>

  <!-- pillar: profitability -->
  <g class="pillar pillar-profit">
    <path d="M549 112 L702 348 L392 348 Z M549 202 L484 303 L614 303 Z" fill="url(#profit-grad)" fill-rule="evenodd"/>
    <path d="M420 303 L674 303 L702 348 L392 348 Z" fill="url(#profit-band)"/>
    <text class="label label-caps" x="539" y="335">PROFITABILITY</text>
    <g class="icon" transform="translate(547 268)">
      <circle class="icon-light" r="15"/>
      <path d="M-9 5 L-3 -2 L2 3 L9 -6" fill="none" stroke="var(--icon-ink)" stroke-width="2.6" stroke-linecap="round" stroke-linejoin="round"/>
      <path d="M4 -6 H9 V-1" fill="none" stroke="var(--icon-ink)" stroke-width="2.6" stroke-linecap="round" stroke-linejoin="round"/>
    </g>
  </g>

  <!-- pillar: partner -->
  <g class="pillar pillar-partner">
    <path d="M220 112 L529 112 L373 348 Z M308 157 L440 157 L373 252 Z" fill="url(#partner-grad)" fill-rule="evenodd" stroke="var(--slide-dark)" stroke-width="6" stroke-linejoin="miter"/>
    <path d="M220 112 L529 112 L499 157 L250 157 Z" fill="url(#partner-band)"/>
    <text class="label label-caps" x="386" y="142">PARTNER</text>
    <g class="icon" transform="translate(373 186)">
      <path class="icon-light" d="M-20 -2 L-10 -12 L-2 -8 L6 -12 L20 -2 L12 6 L4 12 L-4 10 L-12 4 Z"/>
      <path d="M-6 -4 L2 3 M-2 -7 L6 0" stroke="var(--icon-ink)" stroke-width="1.8" stroke-linecap="round"/>
    </g>
  </g>

  <!-- foundation tiles -->
  <g class="tile tile-people">
    <path d="M41 366 L273 366 L159 567 Z" fill="var(--gold)"/>
    <g class="icon" transform="translate(155 414)">
      <circle class="icon-light" cx="0" cy="-9" r="5"/>
      <circle class="icon-light" cx="-11" cy="-5" r="4"/>
      <circle class="icon-light" cx="11" cy="-5" r="4"/>
      <path class="icon-light" d="M-8 12 V2 Q0 -5 8 2 V12 Z M-18 12 V5 Q-14 0 -10 3 V12 Z M18 12 V5 Q14 0 10 3 V12 Z"/>
    </g>
    <text class="label label-tile" x="160" y="453">People</text>
  </g>

  <g class="tile tile-intelligence">
    <path d="M302 366 L418 567 L188 567 Z" fill="var(--gold)"/>
    <g class="icon" transform="translate(302 470)">
      <rect class="icon-light" x="-18" y="-16" width="9" height="9"/>
      <circle class="icon-light" cx="7" cy="-12" r="6"/>
      <rect class="icon-light" x="-17" y="6" width="3" height="8"/>
      <rect class="icon-light" x="-12" y="2" width="3" height="12"/>
      <rect class="icon-light" x="-7" y="-2" width="3" height="16"/>
      <path class="icon-line" d="M1 6 H16 M1 0 L8 -2 H14 M1 12 H14"/>
    </g>
    <text class="label label-tile" x="302" y="513">Business</text>
    <text class="label label-tile" x="302" y="536">Intelligence</text>
  </g>

  <g class="tile tile-innovation">
    <path d="M332 366 L563 366 L448 567 Z" fill="var(--gold)"/>
    <g class="icon" transform="translate(448 408)">
      <path class="icon-light" d="M0 -13 A10 10 0 0 1 6 5 V9 H-6 V5 A10 10 0 0 1 0 -13 Z"/>
      <rect class="icon-light" x="-5" y="11" width="10" height="3"/>
      <path class="icon-line" d="M-16 -4 H-13 M13 -4 H16 M-11 -15 L-9 -13 M11 -15 L9 -13 M0 -20 V-17"/>
    </g>
    <text class="label label-tile" x="449" y="448">Innovation</text>
  </g>

  <g class="tile tile-alliance">
    <path d="M592 366 L708 567 L476 567 Z" fill="var(--gold)"/>
    <g class="icon" transform="translate(590 467)">
      <circle class="icon-line" cx="0" cy="-6" r="12"/>
      <path class="icon-light" d="M-6 -12 H6 V-8 H-6 Z M-4 -7 H4 L5 6 H-5 Z M-8 7 H8 V11 H-8 Z"/>
    </g>
    <text class="label label-tile" x="589" y="513">Strategic</text>
    <text class="label label-tile" x="589" y="536">Alliance</text>
  </g>

  <!-- panel text -->
  <g class="panel-heading">
    <text class="title" x="794" y="235">FIDUCIARY</text>
    <text class="title" x="794" y="274">RESPONSIBILITES</text>
  </g>
  <g class="duty-list">
    <path class="tick" d="M800 310 L807 318 L821 301"/>
    <text class="duty" x="852" y="320">Accurate Financials</text>
    <path class="tick" d="M800 346 L807 354 L821 337"/>
    <text class="duty" x="852" y="356">Internal Controls</text>
    <path class="tick" d="M800 381 L807 389 L821 372"/>
    <text class="duty" x="852" y="391">Brand Protection</text>
    <path class="tick" d="M800 417 L807 425 L821 408"/>
    <text class="duty" x="852" y="427">Compliance</text>
    <path class="tick" d="M800 452 L807 460 L821 443"/>
    <text class="duty" x="852" y="462">Ethics</text>
    <path class="tick" d="M800 488 L807 496 L821 479"/>
    <text class="duty" x="852" y="498">Cost Management</text>
  </g>
</svg>
</body>
</html>
```